Etiketten-Design für Tee-Standbeutel
Zielgruppe
Wir sind ein kleines Café in dem unsere Gäste nicht nur den Kaffee sondern auch unsere natürlichen Tees lieben. Da immer wieder die Nachfrage nach den Tees bestand, möchten wir jetzt den Tee in Standbodenbeutel anbieten.
Kundschaft: Ab 25 Jahre, überwiegend weiblich, Affinität zu Yoga, Wellness, Körperbewusstsein, Gesundheitsbewusst, Premium Tee´s, Entspannung, Meditation, gesunde Ernährung.
Aufgabenstellung
Vorab:
Uns ist wichtig, das auch nach dem Entwurf mit dem Designer zusammen gearbeitet wird. Wenn neue Verpackungen hinzukommen und die Etiketten für die Rückseite gestaltet werden, dann soll dies aus einer Hand kommen.
LogoName:
Kelmanek – Blatt & Sud – Logo von Kelmanek existiert bereits, Blatt & Sud müsste angepasst werden.
Die Idee kam daher, das ich ein Cafe betreibe und die Gäste den Tee gerne auch für zuhause kaufen würden.
Kundschaft:
Ab 25 Jahre, überwiegend weiblich, Affinität zu Yoga, Wellness, Körperbewusstsein, Gesundheitsbewusst, Premium Tee´s, Entspannung, Meditation, gesunde Ernährung
Verpackungsgröße:
kleine Verpackung: 110x185+70mm 250ml/125g
große Verpackung: 130x225+80mm 500ml/ 250g
Das Etikett soll sowohl bei der kleinen als auch bei der großen Packung verwendet werden.
Verpackung:
ist schwarz – Doy Verpackung;
evtl. später Dosen in schwarz
Idee:
Es sind anfänglich ca. 6 verschiedene Teesorten geplant. Etikett soll durch verschiedene Farben den Inhalt des Tees oder Gewürz widerspiegeln
z.B. schwarzer Tee – grau, Kräutertees – grün, Früchtetee – rot, …
Tees:
Verschiedene Kräutertees und Gewürze
Stil:
unkonventionell, individuell, authentisch und alles – außer gewöhnlich
Stil des Sozialrealismus z.B. Parnak - Limonade
kultiges Underground Image
extravagant und anders, hervorhebend
urban style
oder aber:
filigran, schwedischer Stil, helle Farben, dezent und trotzdem ausdrucksstark, einladend

```html
<!DOCTYPE html>
<html lang="de">
<head>
<meta charset="utf-8">
<title>Kelmanek – Blatt &amp; Sud Etiketten</title>
<link href="https://fonts.googleapis.com/css2?family=Oswald:wght@300;400&family=Yellowtail&display=swap" rel="stylesheet">
<style>
  :root {
    --paper: #fefdf8;
    --label: #333333;
    --white: #ffffff;
    --teal: #6ac3ca;
    --rose: #e38d97;
    --lime: #dedb55;
    --lavender: #ada3cf;
  }
  html, body {
    margin: 0;
    padding: 0;
    overflow: hidden;
  }
  .canvas {
    position: relative;
    width: 1200px;
    height: 1200px;
    background: var(--paper);
    overflow: hidden;
  }
  .label {
    position: absolute;
    top: 501px;
    width: 159px;
    height: 198px;
    background: var(--label);
    --accent: var(--teal);
  }
  .label--abwehr { left: 171px; --accent: var(--teal); }
  .label--wiese { left: 406px; --accent: var(--rose); }
  .label--alm { left: 643px; --accent: var(--lime); }
  .label--heiter { left: 879px; --accent: var(--lavender); }

  .brand-dot {
    position: absolute;
    left: 50%;
    top: 22px;
    width: 76px;
    height: 76px;
    margin-left: -38px;
    border-radius: 50%;
    background: var(--accent);
  }
  .brand-name {
    position: absolute;
    left: 0;
    right: 0;
    top: 96px;
    margin: 0;
    text-align: center;
    font-family: "Oswald", sans-serif;
    font-weight: 300;
    font-size: 32px;
    line-height: 36px;
    letter-spacing: 0;
    text-transform: uppercase;
    color: var(--accent);
  }
  .brand-tagline {
    position: absolute;
    left: 0;
    right: 0;
    top: 130px;
    margin: 0;
    text-align: center;
    font-family: "Oswald", sans-serif;
    font-weight: 400;
    font-size: 12px;
    line-height: 14px;
    letter-spacing: 0.8px;
    text-transform: uppercase;
    color: var(--white);
  }
  .flavour-band {
    position: absolute;
    left: 0;
    right: 0;
    bottom: 0;
    height: 35px;
    background: var(--accent);
    display: flex;
    align-items: center;
    justify-content: center;
  }
  .flavour-name {
    margin: 0;
    font-family: "Yellowtail", "Brush Script MT", cursive;
    font-size: 16px;
    line-height: 1;
    white-space: nowrap;
    color: var(--white);
  }
</style>
</head>
<body>
<main class="canvas">
  <article class="label label--abwehr">
    <span class="brand-dot" aria-hidden="true"></span>
    <p class="brand-name">Kelmanek</p>
    <p class="brand-tagline">Blatt &amp; Sud</p>
    <div class="flavour-band"><p class="flavour-name">Abwehr Klar</p></div>
  </article>

  <article class="label label--wiese">
    <span class="brand-dot" aria-hidden="true"></span>
    <p class="brand-name">Kelmanek</p>
    <p class="brand-tagline">Blatt &amp; Sud</p>
    <div class="flavour-band"><p class="flavour-name">Blütenwiese</p></div>
  </article>

  <article class="label label--alm">
    <span class="brand-dot" aria-hidden="true"></span>
    <p class="brand-name">Kelmanek</p>
    <p class="brand-tagline">Blatt &amp; Sud</p>
    <div class="flavour-band"><p class="flavour-name">Almgarten</p></div>
  </article>

  <article class="label label--heiter">
    <span class="brand-dot" aria-hidden="true"></span>
    <p class="brand-name">Kelmanek</p>
    <p class="brand-tagline">Blatt &amp; Sud</p>
    <div class="flavour-band"><p class="flavour-name">Heiterer Tag</p></div>
  </article>
</main>
</body>
</html>
```